Tirel Coffee Beans

I need a label design for our coffee beans brand. The labels would be stuck on a neutral black valve packaging. The labels have a size of 10 × 20 cm.
1 variety: Café Morva 60/40
2 variety: Café Dunrik 70/30
3 variety: Café Brama 80/20
4 variety: Café Tessk 100%
5 varieties: Espresso Movalo 50/50
6 varieties: Espresso Bradimo 60/40
7 variety: Espresso Tarlie 80/20
8 variety: Kulvo Merastinis (specially roasted for Freddo Espresso / Cappuccino)

For example, 70/30 means 70%Arabica 30%Robusta

every label must say: www.brunaleta.de Brunaleta
Gerwin-Ludmark-Str. 7
42917 Harnfeld, whole roasted coffee beans, store in a cool dry place , But in german (www.brunaleta.de Brunaleta
Gerwin-Ludmark-Str. 7
42917 Harnfeld, whole coffee beans roasted, store in a cool, dry place)

the labels should be plain and all in a different color

Target Market(s)

Coffee beans

Requirements
Must have
• our logo see attachment! the coffee varieties white label black writing! the espresso varieties black label white writing!
Nice to have
• Modern, perhaps with numbers like 70/30 on a large scale
Should not have
• characters

```html
<!DOCTYPE html>
<html lang="de">
<head>
<meta charset="utf-8">
<title>Brunaleta – Etiketten Kaffeebohnen</title>
<link rel="stylesheet" href="https://fonts.googleapis.com/css2?family=Montserrat:wght@400;500;700;800&family=Poppins:wght@600;800&display=swap">
<style>
  :root {
    --page: #ffffff;
    --label-light: #ffffff;
    --label-dark: #000000;
    --ink-dark: #111111;
    --ink-light: #ffffff;
    --morva: #f9d9bd;
    --tessk: #d27b56;
    --brama: #ec9f62;
    --dunrik: #a4673b;
    --kulvo: #6a0d44;
    --movalo: #6c8097;
    --bradimo: #ab8a07;
    --tarlie: #0b6e1e;
  }
  * { box-sizing: border-box; margin: 0; padding: 0; }
  html, body { width: 1115px; height: 1200px; overflow: hidden; background: var(--page); }
  body { position: relative; font-family: "Montserrat", sans-serif; }

  .label {
    position: absolute;
    width: 178px; height: 356px;
    background: var(--label-light);
    color: var(--ink-dark);
    box-shadow: 0 0 0 1px #e6e6e6;
  }
  .label--espresso { background: var(--label-dark); color: var(--ink-light); box-shadow: none; }

  .brand {
    position: absolute; top: 22px; left: 0; right: 0;
    display: flex; align-items: center; justify-content: center; gap: 6px;
  }
  .brand__name { font-family: "Montserrat", sans-serif; font-weight: 500; font-size: 15px; letter-spacing: .5px; }
  .brand__dot { width: 12px; height: 12px; border-radius: 50%; background: currentColor; }

  .variety { position: absolute; top: 91px; left: 0; right: 0; text-align: center; line-height: 1; }
  .variety__kind { display: block; font-weight: 400; font-size: 13px; letter-spacing: .3px; }
  .variety__name { display: block; font-weight: 500; font-size: 23px; margin-top: 2px; letter-spacing: .3px; }
  .variety__name--long { font-size: 20px; }

  .blend { position: absolute; top: 229px; left: 0; right: 0; height: 24px; }
  .blend__swatch { position: absolute; left: 0; top: 0; width: 11px; height: 24px; background: var(--swatch); }
  .blend__ratio { position: absolute; left: 14px; top: 0; font-family: "Poppins", sans-serif; font-weight: 800; font-size: 13.5px; line-height: 15px; }
  .blend__ratio--text { font-size: 11px; }
  .blend__detail { position: absolute; left: 14px; top: 16px; font-size: 6.3px; letter-spacing: .4px; white-space: nowrap; }

  .whole-bean { position: absolute; top: 306px; left: 12px; display: flex; align-items: center; gap: 3px; }
  .whole-bean__icon { width: 14px; height: 9px; border-radius: 50%; background: currentColor; }
  .whole-bean__text { font-family: "Poppins", sans-serif; font-weight: 600; font-size: 5.4px; line-height: 6.4px; letter-spacing: .4px; }

  .imprint { position: absolute; left: 12px; top: 331px; font-size: 2.6px; line-height: 3px; opacity: .75; }
  .web { position: absolute; left: 12px; top: 341px; font-size: 6px; }
  .weight { position: absolute; right: 12px; top: 321px; text-align: right; line-height: 1; }
  .weight__amount { font-family: "Poppins", sans-serif; font-weight: 800; font-size: 16px; }
  .weight__e { font-weight: 400; }
  .weight__care { display: block; font-size: 5.6px; margin-top: 2px; }
</style>
</head>
<body>

<!-- Row: Café varieties -->
<article class="label" style="left:63px;top:217px;--swatch:var(--morva)">
  <div class="brand"><span class="brand__name">BRUNALETA</span><span class="brand__dot"></span></div>
  <h2 class="variety"><span class="variety__kind">CAFÉ</span><span class="variety__name">MORVA</span></h2>
  <div class="blend"><span class="blend__swatch"></span><span class="blend__ratio">60/40</span><span class="blend__detail">60%ARABICA | 40%ROBUSTA</span></div>
  <div class="whole-bean"><span class="whole-bean__icon" role="img" aria-label="Kaffeebohnen-Symbol"></span><span class="whole-bean__text">GANZE GERÖSTETE<br>KAFFEEBOHNEN</span></div>
  <p class="imprint">BRUNALETA<br>Brunaleta Rösterei GbR<br>Gerwin-Ludmark-Str. 7 · 42917 Harnfeld</p>
  <p class="web">www.brunaleta.de</p>
  <p class="weight"><span class="weight__amount"><span class="weight__e">℮</span>1000 g</span><span class="weight__care">Kühl und trocken lagern</span></p>
</article>

<article class="label" style="left:330px;top:217px;--swatch:var(--tessk)">
  <div class="brand"><span class="brand__name">BRUNALETA</span><span class="brand__dot"></span></div>
  <h2 class="variety"><span class="variety__kind">CAFÉ</span><span class="variety__name">TESSK</span></h2>
  <div class="blend"><span class="blend__swatch"></span><span class="blend__ratio">100%</span><span class="blend__detail">100%ARABICA</span></div>
  <div class="whole-bean"><span class="whole-bean__icon" role="img" aria-label="Kaffeebohnen-Symbol"></span><span class="whole-bean__text">GANZE GERÖSTETE<br>KAFFEEBOHNEN</span></div>
  <p class="imprint">BRUNALETA<br>Brunaleta Rösterei GbR<br>Gerwin-Ludmark-Str. 7 · 42917 Harnfeld</p>
  <p class="web">www.brunaleta.de</p>
  <p class="weight"><span class="weight__amount"><span class="weight__e">℮</span>1000 g</span><span class="weight__care">Kühl und trocken lagern</span></p>
</article>

<article class="label" style="left:601px;top:217px;--swatch:var(--brama)">
  <div class="brand"><span class="brand__name">BRUNALETA</span><span class="brand__dot"></span></div>
  <h2 class="variety"><span class="variety__kind">CAFÉ</span><span class="variety__name">BRAMA</span></h2>
  <div class="blend"><span class="blend__swatch"></span><span class="blend__ratio">80/20</span><span class="blend__detail">80%ARABICA | 20%ROBUSTA</span></div>
  <div class="whole-bean"><span class="whole-bean__icon" role="img" aria-label="Kaffeebohnen-Symbol"></span><span class="whole-bean__text">GANZE GERÖSTETE<br>KAFFEEBOHNEN</span></div>
  <p class="imprint">BRUNALETA<br>Brunaleta Rösterei GbR<br>Gerwin-Ludmark-Str. 7 · 42917 Harnfeld</p>
  <p class="web">www.brunaleta.de</p>
  <p class="weight"><span class="weight__amount"><span class="weight__e">℮</span>1000 g</span><span class="weight__care">Kühl und trocken lagern</span></p>
</article>

<article class="label" style="left:875px;top:217px;--swatch:var(--dunrik)">
  <div class="brand"><span class="brand__name">BRUNALETA</span><span class="brand__dot"></span></div>
  <h2 class="variety"><span class="variety__kind">CAFÉ</span><span class="variety__name">DUNRIK</span></h2>
  <div class="blend"><span class="blend__swatch"></span><span class="blend__ratio">70/30</span><span class="blend__detail">70%ARABICA | 30%ROBUSTA</span></div>
  <div class="whole-bean"><span class="whole-bean__icon" role="img" aria-label="Kaffeebohnen-Symbol"></span><span class="whole-bean__text">GANZE GERÖSTETE<br>KAFFEEBOHNEN</span></div>
  <p class="imprint">BRUNALETA<br>Brunaleta Rösterei GbR<br>Gerwin-Ludmark-Str. 7 · 42917 Harnfeld</p>
  <p class="web">www.brunaleta.de</p>
  <p class="weight"><span class="weight__amount"><span class="weight__e">℮</span>1000 g</span><span class="weight__care">Kühl und trocken lagern</span></p>
</article>

<!-- Row: Espresso varieties -->
<article class="label label--espresso" style="left:64px;top:784px;--swatch:var(--kulvo)">
  <div class="brand"><span class="brand__name">BRUNALETA</span><span class="brand__dot"></span></div>
  <h2 class="variety"><span class="variety__kind">KULVO</span><span class="variety__name variety__name--long">MERASTINIS</span></h2>
  <div class="blend"><span class="blend__swatch"></span><span class="blend__ratio blend__ratio--text">SPECIALLY ROASTED FOR</span><span class="blend__detail">FREDDO ESPRESSO / CAPPUCCINO)</span></div>
  <div class="whole-bean"><span class="whole-bean__icon" role="img" aria-label="Kaffeebohnen-Symbol"></span><span class="whole-bean__text">GANZE GERÖSTETE<br>KAFFEEBOHNEN</span></div>
  <p class="imprint">BRUNALETA<br>Brunaleta Rösterei GbR<br>Gerwin-Ludmark-Str. 7 · 42917 Harnfeld</p>
  <p class="web">www.brunaleta.de</p>
  <p class="weight"><span class="weight__amount"><span class="weight__e">℮</span>1000 g</span><span class="weight__care">Kühl und trocken lagern</span></p>
</article>

<article class="label label--espresso" style="left:331px;top:784px;--swatch:var(--movalo)">
  <div class="brand"><span class="brand__name">BRUNALETA</span><span class="brand__dot"></span></div>
  <h2 class="variety"><span class="variety__kind">ESPRESSO</span><span class="variety__name">MOVALO</span></h2>
  <div class="blend"><span class="blend__swatch"></span><span class="blend__ratio">50/50</span><span class="blend__detail">50%ARABICA | 50%ROBUSTA</span></div>
  <div class="whole-bean"><span class="whole-bean__icon" role="img" aria-label="Kaffeebohnen-Symbol"></span><span class="whole-bean__text">GANZE GERÖSTETE<br>KAFFEEBOHNEN</span></div>
  <p class="imprint">BRUNALETA<br>Brunaleta Rösterei GbR<br>Gerwin-Ludmark-Str. 7 · 42917 Harnfeld</p>
  <p class="web">www.brunaleta.de</p>
  <p class="weight"><span class="weight__amount"><span class="weight__e">℮</span>1000 g</span><span class="weight__care">Kühl und trocken lagern</span></p>
</article>

<article class="label label--espresso" style="left:602px;top:784px;--swatch:var(--bradimo)">
  <div class="brand"><span class="brand__name">BRUNALETA</span><span class="brand__dot"></span></div>
  <h2 class="variety"><span class="variety__kind">ESPRESSO</span><span class="variety__name">BRADIMO</span></h2>
  <div class="blend"><span class="blend__swatch"></span><span class="blend__ratio">60/40</span><span class="blend__detail">60%ARABICA | 40%ROBUSTA</span></div>
  <div class="whole-bean"><span class="whole-bean__icon" role="img" aria-label="Kaffeebohnen-Symbol"></span><span class="whole-bean__text">GANZE GERÖSTETE<br>KAFFEEBOHNEN</span></div>
  <p class="imprint">BRUNALETA<br>Brunaleta Rösterei GbR<br>Gerwin-Ludmark-Str. 7 · 42917 Harnfeld</p>
  <p class="web">www.brunaleta.de</p>
  <p class="weight"><span class="weight__amount"><span class="weight__e">℮</span>1000 g</span><span class="weight__care">Kühl und trocken lagern</span></p>
</article>

<article class="label label--espresso" style="left:876px;top:784px;--swatch:var(--tarlie)">
  <div class="brand"><span class="brand__name">BRUNALETA</span><span class="brand__dot"></span></div>
  <h2 class="variety"><span class="variety__kind">ESPRESSO</span><span class="variety__name">TARLIE</span></h2>
  <div class="blend"><span class="blend__swatch"></span><span class="blend__ratio">80/20</span><span class="blend__detail">80%ARABICA | 20%ROBUSTA</span></div>
  <div class="whole-bean"><span class="whole-bean__icon" role="img" aria-label="Kaffeebohnen-Symbol"></span><span class="whole-bean__text">GANZE GERÖSTETE<br>KAFFEEBOHNEN</span></div>
  <p class="imprint">BRUNALETA<br>Brunaleta Rösterei GbR<br>Gerwin-Ludmark-Str. 7 · 42917 Harnfeld</p>
  <p class="web">www.brunaleta.de</p>
  <p class="weight"><span class="weight__amount"><span class="weight__e">℮</span>1000 g</span><span class="weight__care">Kühl und trocken lagern</span></p>
</article>

</body>
</html>
```